Beacon Advisory Website

I currently have a website www.beaconadvisoryinc.example. We are a IT Consulting Company. Our website will pretty much tell out our services. I am looking to enhance my website and make it look more professional. Looking for very classy and Contemporary look and design for my website.

Industry/Entity Type

It Company

```html
<!DOCTYPE html>
<html lang="en">
<head>
<meta charset="utf-8">
<title>Beacon Advisory</title>
<link href="https://fonts.googleapis.com/css2?family=Open+Sans:wght@400;600;700&display=swap" rel="stylesheet">
<style>
:root{
  --brand-blue:#1a9ad6;
  --deep-blue:#1d5aa8;
  --heading-grey:#555b63;
  --text-grey:#444;
  --footer-bg:#262b31;
  --footer-text:#d7dbe0;
  --ring:#a9cbe6;
  --header-bg:#e6eef7;
}
*{margin:0;padding:0;box-sizing:border-box}
html,body{width:802px;height:1200px;overflow:hidden}
body{font-family:"Open Sans",Arial,sans-serif;background:#fff;position:relative;color:var(--text-grey)}
.site-header{height:92px;background:linear-gradient(90deg,#eef2f6,var(--header-bg));display:flex;align-items:center;justify-content:center;gap:10px}
.brand-mark{width:34px;height:34px;border-radius:50%;background:var(--deep-blue)}
.brand-name{font-weight:700;font-size:22px;color:var(--deep-blue);letter-spacing:1px}
.main-nav{height:38px;background:var(--brand-blue);display:flex;align-items:center;padding-left:158px}
.main-nav a{color:#fff;text-decoration:none;font-size:11px;font-weight:600;margin-right:31px;letter-spacing:.2px}
.hero{height:317px;background:linear-gradient(90deg,#b9c8d6 0%,#d2dde6 40%,#9fb8d1 65%,#c6d7e6 100%);position:relative}
.hero-dots{position:absolute;right:10px;bottom:10px;display:flex;gap:5px}
.hero-dots span{width:11px;height:11px;background:#2e6db5}
.hero-dots span.active{background:#fff}
.welcome{text-align:center;padding:28px 64px 0}
.welcome h1{font-size:19px;font-weight:400;color:var(--heading-grey);letter-spacing:.3px}
.welcome h1 b{color:var(--deep-blue);font-weight:600}
.welcome p{font-size:10.4px;line-height:18.7px;margin-top:10px;color:var(--text-grey)}
.services{position:absolute;top:642px;left:0;width:802px;height:270px}
.service{position:absolute;top:0;width:210px}
.service .icon{position:absolute;top:0;width:78px;height:78px;border:1.5px solid var(--ring);border-radius:50%;display:flex;align-items:center;justify-content:center}
.service h2{position:absolute;top:98px;font-size:14.5px;font-weight:400;color:var(--heading-grey);letter-spacing:.3px;white-space:nowrap}
.service p{position:absolute;top:125px;font-size:10.4px;line-height:19px;color:var(--text-grey)}
.service .more{position:absolute;top:209px;font-size:9.6px;font-weight:600;color:#333;text-decoration:none}
.service.featured h2,.service.featured .more{color:var(--brand-blue)}
.site-footer{position:absolute;top:912px;left:0;width:802px;height:288px;background:var(--footer-bg);border-top:3px solid var(--brand-blue);color:var(--footer-text)}
.footer-col{position:absolute;top:40px}
.footer-col h3{font-size:10.4px;font-weight:700;color:#fff;letter-spacing:.3px}
.footer-col ul{list-style:none;margin-top:18px}
.footer-col li{font-size:7.6px;height:23.5px;letter-spacing:.2px}
.contact-row{display:flex;gap:10px;font-size:7.6px;line-height:11px;margin-top:16px}
.contact-row svg{flex:none}
.footer-brand{position:absolute;left:612px;top:92px;display:flex;align-items:center;gap:8px}
.footer-brand .brand-mark{background:#fff;width:36px;height:36px}
.footer-brand .brand-name{color:#fff;font-size:20px}
.socials{position:absolute;left:620px;top:202px;display:flex;gap:6px}
.socials span{width:23px;height:23px;border:1.5px solid #cfd4da;border-radius:50%}
.copyright{position:absolute;left:633px;top:242px;font-size:8.4px}
</style>
</head>
<body>
<header class="site-header">
  <span class="brand-mark"></span>
  <span class="brand-name">BEACON ADVISORY</span>
</header>
<nav class="main-nav">
  <a>COMPANY</a><a>SERVICES</a><a>SOLUTIONS</a><a style="margin-left:4px">RESOURCES</a><a>CAREER</a><a>CONTACT US</a>
</nav>
<section class="hero" role="img" aria-label="Photo of a business professional in a light blue shirt in a bright office">
  <div class="hero-dots"><span></span><span class="active"></span><span></span><span></span></div>
</section>
<section class="welcome">
  <h1>WELCOME TO <b>BEACON</b></h1>
  <p>Today’s IT market is a dynamic, fast-paced industry, with ever-increasing demands. Meeting these demands for over 25 years, Beacon Advisory maintains a global presence, aggressively recruiting expertly qualified IT and Management Professionals from around the world and cultivating key partnerships with corporations to understand their business models end-to-end, with a goal of delivering exceptional client service and ensuring a consistent delivery of the talent needed to drive results.</p>
</section>
<section class="services">
  <div class="service" style="left:60px">
    <div class="icon" style="left:43px">
      <svg width="50" height="30" viewBox="0 0 50 30"><path d="M2 6l9-3 7 9-7 6zM48 6l-9-3-7 9 7 6z" fill="#3a3f45"/><path d="M14 10l9-5 7 3 8 8-4 6-5-2-4 3-5-3z" fill="#3a3f45"/></svg>
    </div>
    <h2 style="left:37px">CONSULTING</h2>
    <p style="width:200px">Beacon Advisory has certified profes-sional consultants to work with you to help increase the business by providing IT services ...</p>
    <a class="more" style="left:2px">Read More.......</a>
  </div>
  <div class="service featured" style="left:311px">
    <div class="icon" style="left:47px">
      <svg width="40" height="40" viewBox="0 0 40 40"><circle cx="20" cy="22" r="11" fill="none" stroke="#1a9ad6" stroke-width="6" stroke-dasharray="4 3"/><circle cx="20" cy="22" r="5" fill="#1a9ad6"/></svg>
    </div>
    <h2 style="left:22px">STAFF AUGMENTATION</h2>
    <p style="width:215px">For years Beacon Advisory as been offering our customers the ability to augment their existing staff ...</p>
    <a class="more">Read More.......</a>
  </div>
  <div class="service" style="left:583px">
    <div class="icon" style="left:31px">
      <svg width="34" height="34" viewBox="0 0 34 34"><circle cx="17" cy="17" r="10" fill="none" stroke="#3a3f45" stroke-width="6" stroke-dasharray="4 3.8"/><circle cx="17" cy="17" r="8" fill="none" stroke="#3a3f45" stroke-width="3"/></svg>
    </div>
    <h2 style="left:35px">OFFSHORE</h2>
    <p style="width:182px">Our Offshore development model has a unique distinction of providing efficient software solutions</p>
    <a class="more" style="left:1px">Read More.......</a>
  </div>
</section>
<footer class="site-footer">
  <div class="footer-col" style="left:67px">
    <h3>INFORMATION</h3>
    <ul><li>COMPANY</li><li>SERVICES</li><li>SOLUTIONS</li><li>RESOURCES</li><li>CAREER</li><li>CONTACT US</li></ul>
  </div>
  <div class="footer-col" style="left:228px">
    <h3>CUSTOMER SERVICE</h3>
    <ul style="padding-left:2px"><li>HELP &amp; CONTACT</li><li>RETURN POLICY</li><li>CAREERS</li><li>AFFILITES</li><li>LEGAL NOTICE</li><li>PRIVACY POLICY</li></ul>
  </div>
  <div class="footer-col" style="left:408px">
    <h3>CONTACT US</h3>
    <div class="contact-row" style="margin-top:14px">
      <svg width="10" height="12" viewBox="0 0 10 12"><path d="M5 0a4 4 0 0 0-4 4c0 3 4 8 4 8s4-5 4-8a4 4 0 0 0-4-4z" fill="#fff"/><circle cx="5" cy="4" r="1.5" fill="#262b31"/></svg>
      <span>418 HARBOR LANE<br>SUITE 12<br>WESTBROOK, NJ 07999</span>
    </div>
    <div class="contact-row" style="margin-top:12px">
      <svg width="11" height="11" viewBox="0 0 11 11"><path d="M2 0l2 3-1 1.5a7 7 0 0 0 3.5 3.5L8 7l3 2-1 2C5 11 0 6 0 1z" fill="#fff"/></svg>
      <span>1 (555) 014 2290</span>
    </div>
    <div class="contact-row" style="margin-top:14px">
      <svg width="13" height="10" viewBox="0 0 13 10"><rect x=".75" y=".75" width="11.5" height="8.5" fill="none" stroke="#fff" stroke-width="1.5"/><path d="M1 1l5.5 4.5L12 1" fill="none" stroke="#fff" stroke-width="1.5"/></svg>
      <span>info@beaconadvisory.example</span>
    </div>
  </div>
  <div class="footer-brand"><span class="brand-mark"></span><span class="brand-name">BEACON ADVISORY</span></div>
  <div class="socials"><span></span><span></span><span></span><span></span><span></span></div>
  <div class="copyright">Copyright @ Beacon Advisory</div>
</footer>
</body>
</html>
```